Presentation folder and Brochure for Restoration Company
Water, Fire, and Mold Restoration Services
Presentation folder and Brochure for Restoration Company - Emergency Services
Creative Brief
Emergency Services
Homeowners and commercial property owners that have had their home or building damaged.
Folder will be 9.5"x12" when folded in half, and should have inner flaps. We tend to prefer a cooler palette (blues, greys, etc) with a few splashes of red/yellow/orange where needed for fire cleanup services.

```html
<!DOCTYPE html>
<html lang="en">
<head>
<meta charset="utf-8">
<title>KoriB418 Folder and Brochure</title>
<link rel="stylesheet" href="https://fonts.googleapis.com/css2?family=Open+Sans:wght@400;700&display=swap">
<style>
:root{
  --paper:#ffffff;
  --grey-top:#cfd2d4;
  --grey-mid:#e9eaeb;
  --teal:#3a8e97;
  --red:#c8302a;
  --orange:#ef8a1f;
  --ink:#3b3f43;
  --navy:#1f3f73;
  --water:#5d8fb8;
  --fire:#d8622a;
  --house:#9fb3c4;
}
*{box-sizing:border-box;margin:0;padding:0}
html,body{width:1200px;height:566px;overflow:hidden;background:var(--paper)}
body{position:relative;font-family:"Open Sans",Arial,sans-serif;color:var(--ink)}
.panel{position:absolute;overflow:hidden;background:linear-gradient(180deg,var(--grey-top) 0%,var(--grey-mid) 45%,var(--paper) 70%);box-shadow:0 1px 3px rgba(0,0,0,.25)}
.panel svg.bands{position:absolute;left:0;top:0;width:100%;height:100%;z-index:0}
.photo{position:absolute;z-index:1}
.photo.water{background:linear-gradient(135deg,#8fb4d3,var(--water) 60%,#3d6a92)}
.photo.fire{background:linear-gradient(135deg,#f2b24a,var(--fire) 55%,#7a2a14)}
.photo.house{background:linear-gradient(180deg,#c9d6e0,var(--house) 55%,#6f8fa8)}
.heading{position:absolute;z-index:2;font-weight:700;font-size:6px;line-height:1.2;color:var(--ink);white-space:nowrap}
.heading.large{font-size:9px}
.body-copy{position:absolute;z-index:2;font-size:3.4px;line-height:1.35;color:var(--ink)}
.brand{position:absolute;z-index:2;display:flex;align-items:center;gap:3px;font-weight:700;color:var(--navy);white-space:nowrap}
.brand .dot{border-radius:50%;background:var(--teal)}
.contact{position:absolute;z-index:2;font-size:3.2px;line-height:1.3;color:var(--ink)}
.tagline{position:absolute;z-index:2;font-weight:700;color:var(--paper);transform:rotate(-24deg);transform-origin:left top;white-space:nowrap;font-size:9px;letter-spacing:.5px}
</style>
</head>
<body>

<!-- Inside spread: mold -->
<section class="panel" style="left:0;top:0;width:384px;height:264px">
  <svg class="bands" viewBox="0 0 384 264" preserveAspectRatio="none">
    <polygon points="0,196 384,44 384,58 0,210" fill="var(--red)"/>
    <polygon points="0,210 384,58 384,66 0,218" fill="var(--orange)"/>
    <polygon points="160,264 384,150 384,264" fill="var(--teal)"/>
  </svg>
  <div class="photo water" style="left:250px;top:40px;width:134px;height:110px" role="img" aria-label="Photo of flood water and damaged interior"></div>
  <div class="heading" style="left:210px;top:8px">Water, Fire, and Mold Restoration Services</div>
  <div class="heading" style="left:14px;top:34px">Mold Restoration Services</div>
  <p class="body-copy" style="left:14px;top:46px;width:110px">Mold is found, contained and removed safely so your property is healthy again. We dry, clean and restore homes and businesses after water damage, working fast to limit loss and get you back inside.</p>
  <p class="contact" style="left:8px;top:158px;width:60px">24/7 Emergency Line 555-0142</p>
  <div class="brand" style="left:14px;top:210px;font-size:10px"><span class="dot" style="width:9px;height:9px"></span>KoriB418</div>
</section>

<!-- Inside spread: fire and water -->
<section class="panel" style="left:0;top:283px;width:384px;height:283px">
  <svg class="bands" viewBox="0 0 384 283" preserveAspectRatio="none">
    <polygon points="0,96 384,40 384,48 0,104" fill="var(--red)"/>
    <polygon points="0,104 384,48 384,54 0,110" fill="var(--orange)"/>
    <polygon points="120,283 384,150 384,283" fill="var(--teal)"/>
  </svg>
  <div class="photo fire" style="left:0;top:112px;width:110px;height:150px" role="img" aria-label="Photo of a house fire"></div>
  <div class="photo house" style="left:110px;top:130px;width:120px;height:90px" role="img" aria-label="Photo of a flooded house"></div>
  <div class="heading" style="left:14px;top:14px">Fire Restoration Services</div>
  <p class="body-copy" style="left:14px;top:26px;width:120px">Our crews remove smoke, soot and odor after a fire and rebuild what was lost with care.</p>
  <div class="heading" style="left:230px;top:10px">Water Restoration Services</div>
  <p class="body-copy" style="left:230px;top:22px;width:130px">We dry, clean and restore homes and businesses after water damage, working fast to limit loss and get you back inside.</p>
  <div class="tagline" style="left:250px;top:262px">Fast Response</div>
</section>

<!-- Front cover -->
<section class="panel" style="left:408px;top:144px;width:168px;height:276px">
  <svg class="bands" viewBox="0 0 168 276" preserveAspectRatio="none">
    <polygon points="0,170 168,120 168,130 0,180" fill="var(--red)"/>
    <polygon points="0,180 168,130 168,136 0,186" fill="var(--orange)"/>
    <polygon points="0,236 168,170 168,276 0,276" fill="var(--teal)"/>
  </svg>
  <div class="photo water" style="left:110px;top:40px;width:58px;height:80px" role="img" aria-label="Collage of water and fire damage photos"></div>
  <div class="heading" style="left:8px;top:12px;font-size:5px">Water, Fire, and Mold Restoration Services</div>
  <div class="brand" style="left:10px;top:100px;font-size:12px"><span class="dot" style="width:10px;height:10px"></span>KoriB418</div>
</section>

<!-- Back cover -->
<section class="panel" style="left:653px;top:144px;width:134px;height:276px">
  <svg class="bands" viewBox="0 0 134 276" preserveAspectRatio="none">
    <polygon points="0,170 134,128 134,138 0,180" fill="var(--red)"/>
    <polygon points="0,180 134,138 134,144 0,186" fill="var(--orange)"/>
    <polygon points="0,236 134,180 134,276 0,276" fill="var(--teal)"/>
  </svg>
  <div class="photo fire" style="left:86px;top:40px;width:48px;height:84px" role="img" aria-label="Collage of fire and water damage photos"></div>
  <div class="heading" style="left:6px;top:12px;font-size:5px">Water, Fire, and Mold Restoration Services</div>
</section>

<!-- Brochure outside -->
<section class="panel" style="left:792px;top:0;width:408px;height:276px">
  <svg class="bands" viewBox="0 0 408 276" preserveAspectRatio="none">
    <polygon points="0,100 408,50 408,58 0,108" fill="var(--red)"/>
    <polygon points="0,108 408,58 408,64 0,114" fill="var(--orange)"/>
    <polygon points="150,276 408,110 408,276" fill="var(--teal)"/>
  </svg>
  <div class="photo fire" style="left:0;top:116px;width:110px;height:145px" role="img" aria-label="Photo of a house fire"></div>
  <div class="photo house" style="left:110px;top:124px;width:130px;height:96px" role="img" aria-label="Photo of a flooded house"></div>
  <div class="heading" style="left:12px;top:12px">Fire Restoration Services</div>
  <p class="body-copy" style="left:12px;top:24px;width:120px">Our crews remove smoke, soot and odor after a fire and rebuild what was lost with care.</p>
  <div class="heading" style="left:290px;top:10px">Water Restoration Services</div>
  <p class="body-copy" style="left:250px;top:22px;width:140px">We dry, clean and restore homes and businesses after water damage, working fast to limit loss and get you back inside.</p>
  <div class="tagline" style="left:270px;top:250px">Fast Response</div>
</section>

<!-- Brochure inside -->
<section class="panel" style="left:792px;top:288px;width:408px;height:278px">
  <svg class="bands" viewBox="0 0 408 278" preserveAspectRatio="none">
    <polygon points="0,110 408,70 408,78 0,118" fill="var(--red)"/>
    <polygon points="0,118 408,78 408,84 0,124" fill="var(--orange)"/>
    <polygon points="130,278 408,130 408,278" fill="var(--teal)"/>
  </svg>
  <div class="photo house" style="left:0;top:126px;width:150px;height:106px" role="img" aria-label="Photo of a flooded house"></div>
  <div class="heading" style="left:12px;top:22px">Mold Restoration Services</div>
  <p class="body-copy" style="left:12px;top:34px;width:110px">Mold is found, contained and removed safely so your property is healthy again.</p>
  <div class="heading large" style="left:200px;top:14px">Emergency<br>Services</div>
  <p class="body-copy" style="left:200px;top:42px;width:130px">Call any hour, any day. A trained team is on the way when disaster strikes.</p>
  <div class="brand" style="left:280px;top:150px;font-size:11px"><span class="dot" style="width:9px;height:9px"></span>KoriB418</div>
  <p class="contact" style="left:280px;top:168px;width:60px">24/7 Emergency Line 555-0142</p>
</section>

</body>
</html>
```